RTV CRAFTED

building services
decks
pergola
renovation
extensions
general building

Target Market(s)

middle to upper class

Industry/Entity Type

building

Contact Information for Business Card

my details 0427839152 pkharlow47@mailvane.net BLD574926

Font styles to use
Serif

Colors
00AB8E
00BBA5
67D7C9
C6EFE9
E9F9F6

Requirements
Must have
• logo on the front and details on the back
Nice to have
• sharp and clean lines

```html
<!DOCTYPE html>
<html lang="en">
<head>
<meta charset="utf-8">
<title>RTV Crafted – Business Card</title>
<link rel="stylesheet" href="https://fonts.googleapis.com/css2?family=Tinos:wght@400;700&family=Arimo:wght@400&display=swap">
<style>
  :root{
    --teal:#41aaa8;
    --teal-dark:#1f5f5d;
    --sky:#b5d5e5;
    --ink:#111;
    --grey:#555;
    --paper:#fff;
    --edge:#9a9a9a;
  }
  *{margin:0;padding:0;box-sizing:border-box}
  html,body{width:1200px;height:1200px;overflow:hidden;background:var(--paper)}
  .canvas{position:relative;width:1200px;height:1200px}
  .card{position:absolute;left:338px;width:523px;height:330px;border-radius:8px;overflow:hidden}
  .card-front{top:226px;background:var(--teal)}
  .brand-name{position:absolute;left:0;right:0;top:362px;top:136px;text-align:center;
    font-family:'Tinos',serif;font-weight:400;font-size:43px;letter-spacing:0.5px;color:var(--ink);line-height:1}
  .services{position:absolute;left:0;right:0;top:234px;text-align:center;
    font-family:'Arimo',sans-serif;font-size:16px;color:var(--paper);word-spacing:1px}
  .card-back{top:643px;background:var(--paper);border:1px solid var(--edge)}
  .back-art{position:absolute;inset:0;width:100%;height:100%}
  .holder-name{position:absolute;left:42px;top:52px;font-family:'Tinos',serif;font-size:21px;letter-spacing:1px;color:var(--ink)}
  .holder-role{position:absolute;left:42px;top:77px;font-family:'Arimo',sans-serif;font-size:13px;color:var(--grey)}
  .contact-list{position:absolute;left:40px;top:218px;list-style:none}
  .contact-item{display:flex;align-items:center;height:28px;font-family:'Arimo',sans-serif;font-size:18px;color:var(--grey)}
  .contact-icon{width:16px;height:16px;margin-right:16px;flex:none}
  .emblem-area{position:absolute;left:402px;top:212px;width:88px;height:82px;border-radius:4px;background:#5cb8b6}
</style>
</head>
<body>
<div class="canvas">
  <section class="card card-front">
    <div class="brand-name">RTV CRAFTED</div>
    <div class="services">Renovation | Building Services |&nbsp; Extensions</div>
  </section>

  <section class="card card-back">
    <svg class="back-art" viewBox="0 0 842 531" preserveAspectRatio="none" aria-hidden="true">
      <path d="M513,0 C590,60 650,130 701,204 C728,150 745,80 746,0 Z" fill="var(--sky)"/>
      <path d="M752,0 C748,200 620,360 438,531 L842,531 L842,0 Z" fill="var(--teal)"/>
      <path d="M749,0 C745,200 617,360 435,531" fill="none" stroke="var(--paper)" stroke-width="6"/>
      <path d="M605,394 C560,450 520,490 468,531 L486,531 C530,490 572,445 605,394 Z" fill="var(--teal-dark)"/>
    </svg>
    <div class="holder-name">P. K. Harlow</div>
    <div class="holder-role">CEO/Owner</div>
    <ul class="contact-list">
      <li class="contact-item">
        <svg class="contact-icon" viewBox="0 0 24 24"><path d="M6 2l4 5-2 3c1.5 3 3.5 5 6 6l3-2 5 4-2 4C11 22 2 13 2 4z" fill="none" stroke="var(--teal)" stroke-width="2"/></svg>
        042-783-9152
      </li>
      <li class="contact-item">
        <svg class="contact-icon" viewBox="0 0 24 24"><rect x="4" y="4" width="16" height="11" fill="none" stroke="var(--teal)" stroke-width="2"/><rect x="1" y="17" width="22" height="3" rx="1" fill="var(--teal)"/></svg>
        pkharlow47@mailvane.net
      </li>
      <li class="contact-item">
        <svg class="contact-icon" viewBox="0 0 24 24"><path d="M12 23s-8-8-8-13a8 8 0 0 1 16 0c0 5-8 13-8 13z" fill="var(--teal)"/><circle cx="12" cy="10" r="3.2" fill="var(--paper)"/></svg>
        Address Line
      </li>
    </ul>
    <div class="emblem-area" role="img" aria-label="Company emblem placeholder"></div>
  </section>
</div>
</body>
</html>
```